The Brambury Firm

We need a new design for our letterhead and envelopes. We are a personal injury and criminal defense firm so we need something modern and clean, but more on the professional/traditional side. Our new logo has two colors and is attached to the file so we need something that works well with those colors/matches the design. The following information needs to be on the letterhead:
Phone: (555) 314-7265
Fax: (555) 419-6032
Toll-Free: (555) 736-1149
Post Office Box 4273
Lexington, SC 29458-4273
TQHarmClaimsDesk.example
PalmettoShieldCounsel.example

Target Market(s)

Clients, government agencies, other law firms

Industry/Entity Type

Legal

Font styles to use
Sans Serif
Other font styles liked:
• Arial

Colors

Designer to choose colors to be used in the design.

Requirements
Must have
• Must look professional and clean, modern
Nice to have
• I would like to see a design that works with the logo but does not distract from the content that will be printed on it
Should not have
• Too many colors or crazy designs.

```html
<!DOCTYPE html>
<html lang="en">
<head>
<meta charset="utf-8">
<title>The Brambury Firm — Letterhead</title>
<link href="https://fonts.googleapis.com/css2?family=Open+Sans:wght@400;600&display=swap" rel="stylesheet">
<style>
  :root {
    --backdrop: #e4e4e4;
    --paper: #ffffff;
    --brand-blue: #2b3190;
    --brand-red: #d71c24;
    --ink-grey: #555a60;
  }
  html, body {
    margin: 0;
    padding: 0;
    width: 1200px;
    height: 1200px;
    overflow: hidden;
    background: var(--backdrop);
    font-family: "Open Sans", Arial, sans-serif;
  }
  .letterhead {
    position: absolute;
    left: 175px;
    top: 50px;
    width: 850px;
    height: 1100px;
    background: var(--paper);
    box-shadow: 0 2px 10px rgba(0,0,0,0.12);
    overflow: hidden;
  }
  .firm-name {
    position: absolute;
    left: 58px;
    top: 64px;
    display: flex;
    align-items: center;
    gap: 10px;
    margin: 0;
    font-size: 26px;
    font-weight: 600;
    color: var(--brand-blue);
    letter-spacing: 0.5px;
  }
  .firm-name .mark {
    width: 16px;
    height: 16px;
    border-radius: 50%;
    background: var(--brand-red);
  }
  .contact-block {
    position: absolute;
    left: 560px;
    top: 58px;
    font-size: 10.5px;
    line-height: 15px;
    color: var(--ink-grey);
  }
  .contact-block .address { margin: 0 0 2px; }
  .contact-block ul {
    list-style: none;
    margin: 0;
    padding: 0 0 0 14px;
  }
  .contact-block li {
    display: flex;
    align-items: center;
    gap: 6px;
  }
  .contact-block svg {
    width: 9px;
    height: 9px;
    fill: var(--brand-red);
    flex: none;
  }
  .footer-band {
    position: absolute;
    left: 0;
    bottom: 0;
    width: 850px;
    height: 14px;
  }
</style>
</head>
<body>
  <main class="letterhead">
    <h1 class="firm-name"><span class="mark"></span>The Brambury Firm</h1>

    <address class="contact-block">
      <p class="address">P.O. Box 4273 Lexington,<br>SC 29458-4273</p>
      <ul>
        <li>
          <svg viewBox="0 0 10 10" aria-hidden="true"><path d="M2 0.5 L3.6 0.5 L4.2 3 L3 3.8 Q4 6 6.2 7 L7 5.8 L9.5 6.4 L9.5 8 Q9.5 9.5 8 9.5 Q0.5 9 0.5 2 Q0.5 0.5 2 0.5Z"/></svg>
          (555) 314-7265
        </li>
        <li>
          <svg viewBox="0 0 10 10" aria-hidden="true"><rect x="2.5" y="0.5" width="5" height="3"/><rect x="0.5" y="3.5" width="9" height="4" rx="0.8"/><rect x="2.5" y="7" width="5" height="2.5"/></svg>
          (555) 419-6032
        </li>
        <li>
          <svg viewBox="0 0 10 10" aria-hidden="true"><path d="M2 0.5 L3.6 0.5 L4.2 3 L3 3.8 Q4 6 6.2 7 L7 5.8 L9.5 6.4 L9.5 8 Q9.5 9.5 8 9.5 Q0.5 9 0.5 2 Q0.5 0.5 2 0.5Z"/></svg>
          (555) 736-1149 (Toll-Free)
        </li>
        <li>
          <svg viewBox="0 0 10 10" aria-hidden="true"><circle cx="5" cy="5" r="4.3" fill="none" stroke="#d71c24" stroke-width="1"/><ellipse cx="5" cy="5" rx="1.8" ry="4.3" fill="none" stroke="#d71c24" stroke-width="0.8"/><line x1="0.7" y1="5" x2="9.3" y2="5" stroke="#d71c24" stroke-width="0.8"/></svg>
          TQHarmClaimsDesk.example
        </li>
        <li>
          <svg viewBox="0 0 10 10" aria-hidden="true"><circle cx="5" cy="5" r="4.3" fill="none" stroke="#d71c24" stroke-width="1"/><ellipse cx="5" cy="5" rx="1.8" ry="4.3" fill="none" stroke="#d71c24" stroke-width="0.8"/><line x1="0.7" y1="5" x2="9.3" y2="5" stroke="#d71c24" stroke-width="0.8"/></svg>
          PalmettoShieldCounsel.example
        </li>
      </ul>
    </address>

    <svg class="footer-band" viewBox="0 0 850 14" preserveAspectRatio="none" aria-hidden="true">
      <polygon points="0,0 440,0 448,7 440,14 0,14" fill="var(--brand-blue)"/>
      <polygon points="444,0 850,0 850,14 444,14 452,7" fill="var(--brand-red)"/>
    </svg>
  </main>
</body>
</html>
```